4月よりリリースされる写真販売サイトの、クライアント管理画面に表示するボタンの作成依頼です。
クライアントは保育園が多い為、女性受けする可愛いデザインで、お願いします。
色はお任せします。
カラフルな楽しいイメージにしたいです。

以下、5種類のボタンの作成をお願いします

・写真の展示をする
・既にある写真展示室を編集する
・売上状況や注文ランキングを確認する
・売上代金の振込依頼をする
・管理者へ連絡・質問する

ボタンに、項目を連想するようなイラストもお願いします。
・写真の展示をする → 写真のイラスト
・既にある写真展示室を編集する → 消しゴム等のイラスト
・売上状況や注文ランキングを確認する → グラフのイラスト
・売上代金の振込依頼をする → 銀行やお金のイラスト
・管理者へ連絡・質問する → メールのイラスト
お任せします
• 高解像度JPG (.jpg)
• イラストレーター形式 (.ai)
• フォトショップ形式 (.psd)
• PNG形式 (.png)
URLです
http://kazetoyumehana.com/
一つ記入漏れがありましたので追記します。

過去の写真をもう一度展示する  というボタンが抜けておりました。

イラストは、再展示がイメージできるような感じであれば問題ありませんのでお任せいたします。

イメージ通りでした。

皆様、たくさんの素敵なデザインありがとうございます。今後ともよろしくお願いいたします。

```html
<!DOCTYPE html>
<html lang="ja">
<head>
<meta charset="utf-8">
<title>管理メニュー</title>
<link rel="stylesheet" href="https://fonts.googleapis.com/css2?family=M+PLUS+Rounded+1c:wght@700&display=swap">
<style>
  :root {
    --bg: #ffffff;
    --salmon: #f0877b;
    --sky: #7fd3ee;
    --grape: #9a5aa8;
    --leaf: #8fc86b;
    --peach: #f8ad79;
    --mustard: #e2c45f;
    --text: #ffffff;
    --shade: rgba(0, 0, 0, 0.18);
    --frame: #ffffff;
    --mail: #7fd0ee;
  }
  * { margin: 0; padding: 0; box-sizing: border-box; }
  html, body {
    width: 826px; height: 1200px; overflow: hidden;
    background: var(--bg);
  }
  .menu {
    position: absolute; left: 33px; top: 41px;
    width: 760px;
    display: flex; flex-direction: column; gap: 11px;
  }
  .menu-button {
    position: relative;
    height: 172px;
    border-radius: 12px;
    display: flex; align-items: center;
    text-decoration: none;
  }
  .menu-button--exhibit { background: var(--salmon); }
  .menu-button--sales { background: var(--sky); }
  .menu-button--edit { background: var(--grape); }
  .menu-button--reexhibit { background: var(--leaf); }
  .menu-button--transfer { background: var(--peach); }
  .menu-button--contact { background: var(--mustard); }
  .menu-icon {
    position: absolute; left: 40px; top: 26px;
    width: 140px; height: 120px;
    display: flex; align-items: center; justify-content: center;
  }
  .illustration { border-radius: 14px; }
  .illustration--photo { width: 128px; height: 100px; background: linear-gradient(180deg, #f6d7d2 0%, #fbe9e6 100%); }
  .illustration--chart { width: 130px; height: 110px; background: linear-gradient(180deg, #c9ecf7 0%, #a9dcee 100%); }
  .illustration--stationery { width: 124px; height: 116px; background: linear-gradient(135deg, #f4a25b 0%, #f1c85c 45%, #dfe9f2 55%, #79c8e8 100%); border-radius: 30px; }
  .illustration--photos { width: 130px; height: 110px; background: linear-gradient(160deg, #ffffff 0%, #e9e3de 40%, #8c7f79 100%); border-radius: 10px; }
  .illustration--purse { width: 120px; height: 108px; background: radial-gradient(circle at 50% 60%, #f46f6a 0%, #ef5f5e 70%, #e2534f 100%); border-radius: 46% 46% 40% 40%; }
  .menu-label {
    position: absolute; left: 230px; right: 20px;
    color: var(--text);
    font-family: "M PLUS Rounded 1c", sans-serif;
    font-weight: 700; font-size: 42px; letter-spacing: 1px;
    text-align: center;
    text-shadow: 2px 2px 3px var(--shade);
    white-space: nowrap;
  }
</style>
</head>
<body>
<nav class="menu">
  <a class="menu-button menu-button--exhibit" href="#">
    <span class="menu-icon"><span class="illustration illustration--photo" role="img" aria-label="写真のイラスト"></span></span>
    <span class="menu-label">写真を展示する</span>
  </a>
  <a class="menu-button menu-button--sales" href="#">
    <span class="menu-icon"><span class="illustration illustration--chart" role="img" aria-label="売上グラフのイラスト"></span></span>
    <span class="menu-label">売上・ランキングを見る</span>
  </a>
  <a class="menu-button menu-button--edit" href="#">
    <span class="menu-icon"><span class="illustration illustration--stationery" role="img" aria-label="鉛筆と消しゴムのイラスト"></span></span>
    <span class="menu-label">写真展示室を編集する</span>
  </a>
  <a class="menu-button menu-button--reexhibit" href="#">
    <span class="menu-icon"><span class="illustration illustration--photos" role="img" aria-label="重なった写真のイラスト"></span></span>
    <span class="menu-label">過去写真を展示する</span>
  </a>
  <a class="menu-button menu-button--transfer" href="#">
    <span class="menu-icon"><span class="illustration illustration--purse" role="img" aria-label="円マークのがま口財布のイラスト"></span></span>
    <span class="menu-label">振込を依頼する</span>
  </a>
  <a class="menu-button menu-button--contact" href="#">
    <span class="menu-icon">
      <svg width="140" height="100" viewBox="0 0 140 100" aria-hidden="true">
        <rect x="4" y="8" width="132" height="86" rx="6" fill="var(--mail)"/>
        <polyline points="8,12 70,60 132,12" fill="none" stroke="var(--frame)" stroke-width="7" stroke-linejoin="round"/>
      </svg>
    </span>
    <span class="menu-label">お問い合わせ</span>
  </a>
</nav>
</body>
</html>
```